Brightfold Systems, a software development company, needs a website

We need a website to promote our software development company. The company is brand new and we want to market ourselves. We develop all kinds of software from web applications, to desktop applications, to mobile applications. Small company, not a lot of history, just need something flashy.

```html
<!DOCTYPE html>
<html lang="en">
<head>
<meta charset="utf-8">
<title>Brightfold Systems Inc</title>
<link rel="stylesheet" href="https://fonts.googleapis.com/css2?family=Montserrat:wght@400;500;600&family=Lato:wght@400;700&display=swap">
<style>
:root{
  --navy:#0a1a31;
  --navy-deep:#071426;
  --orange:#f07f1c;
  --blue:#1b5a8c;
  --ink:#1f2329;
  --muted:#8b8f95;
  --light:#f4f5f7;
  --footer:#1f2124;
  --white:#ffffff;
  --grad:linear-gradient(90deg,#f07f1c 0%,#1b5a8c 100%);
}
*{box-sizing:border-box;margin:0;padding:0}
html,body{width:1200px;height:4729px;overflow:hidden}
body{position:relative;background:var(--white);font-family:'Lato',sans-serif;color:var(--ink)}
.abs{position:absolute}
.heading{font-family:'Montserrat',sans-serif}

/* hero */
.hero{left:0;top:0;width:1200px;height:677px;background:linear-gradient(160deg,#3a3430 0%,#2a2622 45%,#4a3f35 75%,#1e1b19 100%)}
.hero-shade{left:0;top:0;width:1200px;height:677px;background:rgba(10,12,16,.55)}
.brand{left:77px;top:34px;color:var(--white);font-family:'Montserrat',sans-serif;line-height:1}
.brand .name{font-size:36px;font-weight:500;letter-spacing:.5px}
.brand .sub{font-size:20px;font-weight:500;letter-spacing:2px;margin-top:8px;padding-left:20px}
.nav{top:70px;left:0;width:1200px;font-family:'Lato',sans-serif;font-size:16px;color:var(--white)}
.nav span{position:absolute}
.nav .active{color:var(--orange)}
.nav-caret{left:522px;top:98px}
.login{left:998px;top:51px;width:125px;height:54px;border-radius:5px;background:var(--grad);color:var(--white);font-family:'Montserrat',sans-serif;font-size:18px;display:flex;align-items:center;justify-content:center}
.hero-title{left:0;top:232px;width:1200px;text-align:center;font-family:'Montserrat',sans-serif;font-size:60px;font-weight:500;color:var(--orange)}
.hero-title .alt{color:var(--blue)}
.hero-sub{left:0;top:308px;width:1200px;text-align:center;color:var(--white);font-size:26px;line-height:32px}
.hero-copy{left:290px;top:392px;width:620px;text-align:center;color:var(--white);font-size:15.5px;line-height:29px}
.dots{left:566px;top:572px;width:70px;height:22px}

/* offering */
.device{left:77px;top:760px;width:484px;height:468px;border-radius:22px 22px 0 0;background:linear-gradient(135deg,#e9edf3 0%,#c9d4e3 55%,#2b3b55 100%)}
.kicker{left:620px;top:757px;color:var(--blue);font-size:21px;font-family:'Montserrat',sans-serif;font-weight:500}
.offer-title{left:620px;top:792px;font-size:37px;font-family:'Montserrat',sans-serif;font-weight:500;color:var(--ink)}
.offer-copy{left:620px;top:858px;width:502px;font-size:14.5px;line-height:25px;color:var(--muted)}
.btn-pill{left:618px;top:1092px;width:145px;height:51px;border-radius:26px;background:var(--grad);color:var(--white);font-family:'Montserrat',sans-serif;font-size:18px;display:flex;align-items:center;justify-content:center}

/* service bands */
.band{left:0;width:1200px;height:563px;background:var(--navy)}
.band-photo{position:absolute;top:0;height:100%;width:100%}
.card{width:396px;height:395px;background:var(--white);padding:77px 36px 0 44px;box-shadow:0 2px 10px rgba(0,0,0,.12)}
.card h3{font-family:'Montserrat',sans-serif;font-weight:500;font-size:30px;color:var(--blue);margin-bottom:26px}
.card p{font-size:14px;line-height:25px;color:var(--muted)}
.card .more{display:block;margin-top:28px;font-family:'Montserrat',sans-serif;font-size:15px;color:var(--orange);font-weight:500}

/* about */
.about-photo{left:0;top:2916px;width:1200px;height:622px;background:linear-gradient(180deg,#dfe6ec 0%,#b9c5d0 40%,#5d6b7a 75%,#2c3440 100%)}
.about-bg{left:0;top:3538px;width:1200px;height:429px;background:var(--light)}
.about-card{left:77px;top:3415px;width:1046px;height:374px;background:var(--white);box-shadow:0 2px 10px rgba(0,0,0,.08);text-align:center}
.about-card h2{position:absolute;left:0;top:62px;width:100%;font-family:'Montserrat',sans-serif;font-weight:500;font-size:41px;color:var(--blue)}
.about-card h2 .alt{color:var(--orange)}
.about-card p{position:absolute;left:160px;top:128px;width:726px;font-size:14px;line-height:25px;color:var(--muted)}
.btn-box{position:absolute;left:450px;top:260px;width:146px;height:51px;border-radius:3px;background:linear-gradient(90deg,#f07f1c,#e2601e);color:var(--white);font-family:'Montserrat',sans-serif;font-size:18px;display:flex;align-items:center;justify-content:center}
.partners{left:77px;top:3858px;width:1046px;height:50px;display:flex;justify-content:space-between;align-items:center}
.partner{display:flex;align-items:center;gap:8px;font-family:'Montserrat',sans-serif;font-weight:600;font-size:22px;color:var(--blue)}
.partner i{display:block;width:16px;height:16px;border-radius:50%;background:var(--blue)}

/* newsletter */
.news-title{left:0;top:4045px;width:1173px;text-align:center;font-family:'Montserrat',sans-serif;font-weight:500;font-size:37px;color:var(--ink)}
.news-sub{left:0;top:4112px;width:1173px;text-align:center;font-size:15.5px;color:#4a4d52}
.field{top:4171px;height:50px;border:1px solid #d8dbdf;background:var(--white);padding-left:18px;display:flex;align-items:center;font-size:13px;color:#a6aab0}
.subscribe{left:743px;top:4171px;width:167px;height:50px;background:var(--grad);color:var(--white);font-family:'Montserrat',sans-serif;font-size:18px;display:flex;align-items:center;justify-content:center}

/* footer */
.footer{left:0;top:4310px;width:1200px;height:419px;background:var(--footer)}
.foot-brand{left:0;top:4386px;width:1200px;text-align:center;color:var(--white);font-family:'Montserrat',sans-serif;line-height:1}
.foot-brand .name{font-size:40px;font-weight:500}
.foot-brand .sub{font-size:21px;font-weight:500;letter-spacing:2px;margin-top:10px}
.foot-links{left:0;top:4486px;width:1200px;text-align:center;color:var(--white);font-size:16px;word-spacing:2px}
.foot-links b{font-weight:400;margin:0 18px}
.social{left:497px;top:4529px;width:206px;height:48px}
.rule{left:0;top:4634px;width:1200px;height:1px;background:#3a3c40}
.copy{left:0;top:4672px;width:1200px;text-align:center;color:#9a9da2;font-size:14px}
.copy strong{color:#c9cbcf;font-weight:700}
</style>
</head>
<body>

<!-- Hero -->
<section class="abs hero" role="img" aria-label="Team working at laptops on a wooden desk, dimmed background photo"></section>
<div class="abs hero-shade"></div>
<div class="abs brand"><div class="name">Brightfold</div><div class="sub">Systems Inc</div></div>
<nav class="abs nav">
  <span class="active" style="left:502px">Home</span>
  <span style="left:595px">About</span>
  <span style="left:694px">Services</span>
  <span style="left:809px">Blog</span>
  <span style="left:892px">Contact</span>
</nav>
<svg class="abs nav-caret" width="12" height="10" viewBox="0 0 12 10"><path d="M6 0 12 10H0z" fill="#f07f1c"/></svg>
<div class="abs login">Log In</div>
<h1 class="abs hero-title">Brightfold <span class="alt">Systems</span></h1>
<p class="abs hero-sub">We're The Best design &amp; Development<br>Copmany In The World</p>
<p class="abs hero-copy">Lorem ipsum dolor sit amet, consectetur adipiscing elit, sed do eiusmod tempor exercitation ullamco laboris nisi ut aliquip ex ea commodo consequat.</p>
<svg class="abs dots" viewBox="0 0 70 22">
  <circle cx="8" cy="11" r="5.5" fill="#fff"/>
  <circle cx="34" cy="11" r="9" fill="none" stroke="#fff" stroke-width="1.5"/>
  <circle cx="34" cy="11" r="6" fill="#f07f1c"/>
  <circle cx="60" cy="11" r="5.5" fill="#fff"/>
</svg>

<!-- Offering -->
<div class="abs device" role="img" aria-label="Tablet and phone showing a responsive website mock-up"></div>
<div class="abs kicker">We'er Offering</div>
<h2 class="abs offer-title">Awesome Customer services</h2>
<p class="abs offer-copy">Lorem ipsum dolor sit amet, consectetur adipiscing elit, sed do eiusmod they tempor incididunt ut labore et dolore magna aliqua. Ut enim ad minim therer veniam, quis nostrud exercitation ullamco laboris nisi ut aliquip ex ea of there commodo consequat. Duis aute irure dolor in reprehenderit in voluptate the velit esse cillum dolore eu fugiat nulla pariatur. Excepteur sint occaecat of to cupidatat non proident, sunt in culpa qui officia deserunt mollit anim id est laborum. Nor again is there anyone who loves or pursues or desires to obtain pain of itself, because it is pain, but because occasionally.</p>
<div class="abs btn-pill">Get Started</div>

<!-- Web Applications -->
<section class="abs band" style="top:1228px">
  <div class="band-photo" role="img" aria-label="Two developers reviewing code on a monitor" style="clip-path:polygon(27% 0,100% 0,100% 100%,37% 100%);background:linear-gradient(120deg,#24374b 0%,#4d6275 40%,#9aa6ad 75%,#cfd4d4 100%)"></div>
  <div class="abs card" style="left:77px;top:84px">
    <h3>Web Applications</h3>
    <p>Lorem ipsum dolor sit am, consectetur adipiscing elit, sed do eiusmod tempor incididunt ut labore et dolore magna aliqua. Ut enim ad mini veniam, quis nostrud exercitation ullamco laboris nisi ut aliquip ex ea commodo consequat.</p>
    <span class="more">Read More</span>
  </div>
</section>

<!-- Mobile Applications -->
<section class="abs band" style="top:1791px">
  <div class="band-photo" role="img" aria-label="Hand holding a smartphone with a booking app" style="clip-path:polygon(0 0,65% 0,58% 100%,0 100%);background:linear-gradient(120deg,#3b2c22 0%,#7a5f48 40%,#b49a80 70%,#6d5a4b 100%)"></div>
  <div class="abs card" style="left:727px;top:83px">
    <h3>Mobile Applications</h3>
    <p>Lorem ipsum dolor sit am, consectetur adipiscing elit, sed do eiusmod tempor incididunt ut labore et dolore magna aliqua. Ut enim ad mini veniam, quis nostrud exercitation ullamco laboris nisi ut aliquip ex ea commodo consequat.</p>
    <span class="more">Read More</span>
  </div>
</section>

<!-- Desktop Applications -->
<section class="abs band" style="top:2352px">
  <div class="band-photo" role="img" aria-label="Laptop displaying analytics dashboard on an office desk" style="clip-path:polygon(28% 0,100% 0,100% 100%,36% 100%);background:linear-gradient(120deg,#c4ccd3 0%,#e6e9ec 45%,#9aa3ab 80%,#5e6770 100%)"></div>
  <div class="abs card" style="left:77px;top:85px">
    <h3>Desktop Applications</h3>
    <p>Lorem ipsum dolor sit am, consectetur adipiscing elit, sed do eiusmod tempor incididunt ut labore et dolore magna aliqua. Ut enim ad mini veniam, quis nostrud exercitation ullamco laboris nisi ut aliquip ex ea commodo consequat.</p>
    <span class="more">Read More</span>
  </div>
</section>

<!-- About -->
<div class="abs about-photo" role="img" aria-label="Business partners shaking hands across a meeting table"></div>
<div class="abs about-bg"></div>
<section class="abs about-card">
  <h2>About <span class="alt">Brightfold Systems</span></h2>
  <p>Lorem ipsum dolor sit amet, consectetur adipiscing elit, sed do eiusmod tempor incididunt ut labore et dolore magna aliqua. Ut enim ad minim veniam, quis nostrud exercitation ullamco laboris nisi ut aliquip ex ea commodo consequat. Duis aute irure dolor in reprehenderit in voluptate velit esse cillum dolore eu fugiat nulla pariatur. Excepteur sint occaecat cupidatat non proident, sunt in culpa qui officia deserunt</p>
  <div class="btn-box">Get Started</div>
</section>
<div class="abs partners">
  <span class="partner"><i></i>Marlowe</span>
  <span class="partner"><i></i>Nimbuscore</span>
  <span class="partner"><i></i>Vantreon</span>
  <span class="partner"><i></i>Marlowe</span>
  <span class="partner"><i></i>Nimbuscore</span>
  <span class="partner"><i></i>Vantreon</span>
</div>

<!-- Newsletter -->
<h2 class="abs news-title">Sign Up Our Newsletter</h2>
<p class="abs news-sub">To receive email releases, simply provide us with your email below</p>
<div class="abs field" style="left:264px;width:228px">Name :</div>
<div class="abs field" style="left:505px;width:227px">Email :</div>
<div class="abs subscribe">Subcribe Now</div>

<!-- Footer -->
<footer class="abs footer"></footer>
<div class="abs foot-brand"><div class="name">Brightfold</div><div class="sub">Systems Inc</div></div>
<div class="abs foot-links">Home<b>|</b>About<b>|</b>Services<b>|</b>Blog<b>|</b>Contact</div>
<svg class="abs social" viewBox="0 0 206 48" role="img" aria-label="Social network links">
  <circle cx="24" cy="24" r="23" fill="#1b5a8c"/>
  <circle cx="77" cy="24" r="23" fill="#d98a1f"/>
  <circle cx="129" cy="24" r="23" fill="#d98a1f"/>
  <circle cx="182" cy="24" r="23" fill="#d98a1f"/>
</svg>
<div class="abs rule"></div>
<p class="abs copy">Copyright © <strong>Brightfold Systems Inc</strong> - 2019. All Right Reserved</p>

</body>
</html>
```